Cool modern, tech Business card design

Looking for a new business card design for our Managed IT Services company. We would like 2 sides, with the logo one one side horizontally and then the information on the back in either vertical or horizontal. We want our colors from the logo incorporated but also would like to see the color gray in there as well.

Target Market(s)

IT, Information Technology, Tech, Service

Industry/Entity Type

It Service

Contact Information for Business Card

Pavel Lind
Managing Partner
(P)742-318-6650 ext xxx
(F)742-318-6651
www.qelvantrixo.com

Font styles to use
Sans Serif

Colors
959595
000000
ec1f27

Requirements
Must have
• Logo on one side with some nice design or pattern
• Information on back in either vertical or horizontal format
Nice to have
• For it to look cool, tech, modern, stand out.

```html
<!DOCTYPE html>
<html lang="en">
<head>
<meta charset="utf-8">
<title>Qelvantrixo Business Card</title>
<link href="https://fonts.googleapis.com/css2?family=Open+Sans:wght@400;600&display=swap" rel="stylesheet">
<style>
  :root {
    --backdrop: #dedede;
    --card: #1c1c1e;
    --red: #d0192b;
    --white: #ffffff;
    --gray: #959595;
  }
  * { margin: 0; padding: 0; box-sizing: border-box; }
  html, body { width: 1200px; height: 1200px; overflow: hidden; }
  body {
    background: var(--backdrop);
    font-family: "Open Sans", Arial, sans-serif;
    position: relative;
  }
  .card {
    position: absolute;
    left: 258px;
    width: 669px;
    height: 382px;
    background: var(--card);
    overflow: hidden;
  }
  .card--front { top: 170px; }
  .card--back { top: 648px; }
  .edge-bar {
    position: absolute;
    top: 114px;
    width: 7px;
    height: 154px;
    background: var(--red);
  }
  .edge-bar--left { left: 0; }
  .edge-bar--right { right: 0; }

  .brand {
    position: absolute;
    display: flex;
    align-items: center;
    gap: 10px;
    transform: translateX(-50%);
    color: var(--white);
    font-weight: 600;
    letter-spacing: 0.5px;
    white-space: nowrap;
  }
  .brand__square {
    width: 14px;
    height: 14px;
    background: var(--red);
  }
  .card--front .brand { left: 50%; top: 168px; font-size: 34px; }
  .card--back .brand { left: 170px; top: 274px; font-size: 28px; }

  .person {
    position: absolute;
    top: 68px;
    left: 0;
    width: 100%;
    text-align: center;
  }
  .person__name {
    color: var(--white);
    font-size: 24px;
    font-weight: 400;
    line-height: 1.1;
  }
  .person__title {
    color: var(--red);
    font-size: 13px;
    line-height: 1.4;
  }

  .divider {
    position: absolute;
    left: 332px;
    top: 196px;
    width: 2px;
    height: 186px;
    background: var(--white);
  }
  .divider__dot {
    position: absolute;
    left: 327px;
    top: 184px;
    width: 13px;
    height: 13px;
    border-radius: 50%;
    background: var(--red);
  }

  .contacts {
    position: absolute;
    left: 362px;
    top: 242px;
    list-style: none;
  }
  .contacts__link {
    position: absolute;
    left: 372px;
    top: 262px;
    width: 1px;
    height: 50px;
    background: var(--gray);
  }
  .contact {
    display: flex;
    align-items: center;
    gap: 10px;
    height: 31px;
    color: var(--white);
    font-size: 13px;
  }
  .contact__icon {
    width: 19px;
    height: 19px;
    border: 1px solid var(--white);
    border-radius: 50%;
    background: var(--card);
    display: flex;
    align-items: center;
    justify-content: center;
    position: relative;
    z-index: 1;
  }
  .contact__icon svg { width: 10px; height: 10px; }
</style>
</head>
<body>
  <section class="card card--front">
    <div class="edge-bar edge-bar--left"></div>
    <div class="edge-bar edge-bar--right"></div>
    <div class="brand"><span class="brand__name">qelvantrixo</span><span class="brand__square"></span></div>
  </section>

  <section class="card card--back">
    <div class="edge-bar edge-bar--left"></div>
    <div class="edge-bar edge-bar--right"></div>

    <div class="person">
      <h1 class="person__name">Pavel Lind</h1>
      <p class="person__title">Managing Partner</p>
    </div>

    <div class="brand"><span class="brand__name">qelvantrixo</span><span class="brand__square"></span></div>

    <div class="divider"></div>
    <div class="divider__dot"></div>

    <div class="contacts__link"></div>
    <ul class="contacts">
      <li class="contact">
        <span class="contact__icon">
          <svg viewBox="0 0 10 10"><path d="M2 1 L4 1 L4.5 3 L3.3 3.8 Q4.3 5.9 6.2 6.7 L7 5.5 L9 6 L9 8 Q5 9 1.5 5 Q0.8 3 2 1 Z" fill="var(--red)"/></svg>
        </span>
        <span>742-318-6650</span>
      </li>
      <li class="contact">
        <span class="contact__icon">
          <svg viewBox="0 0 10 10"><rect x="3" y="1" width="4" height="3" fill="var(--red)"/><rect x="1" y="4" width="8" height="5" fill="var(--red)"/></svg>
        </span>
        <span>742-318-6651</span>
      </li>
      <li class="contact">
        <span class="contact__icon">
          <svg viewBox="0 0 10 10" fill="none" stroke="var(--red)" stroke-width="1"><circle cx="5" cy="5" r="4"/><ellipse cx="5" cy="5" rx="1.8" ry="4"/><line x1="1" y1="5" x2="9" y2="5"/></svg>
        </span>
        <span>www.qelvantrixo.com</span>
      </li>
    </ul>
  </section>
</body>
</html>
```